Online Advertising agency with fun music culture twist

We need a new website for our online advertising agency. The current site is just a placeholder but you can pull the text from the site- quillmarketbench.com. The new site will be 10 total pages. The current site has 8 pages. So this project will require the design and code for all 10 pages.

Things I like- Clean, easy to read, custom graphics, video,
splash 1-2 colors, futuristic, music twist, fun, interesting, looks amazing on a mobile site, extremely professional design.

Things I don't like- I hate stock graphics, pages that scroll to much, to many colors (rainbow), sites that don't flow, very templated cookie cutter sites, not mobile compliant.

We built a sophisticated buying platform for advertisers to reach the right person on the right device at the right time. I used to be a concert promoter and I have several musicians that work with us. We want to play into the fun and excitement of live music with an advertising twist hence the name Quill. We don't want to make it seem like a music company but we can use subtle vinyl and music references. My other company is meadowpixelworks.com for reference. I really like to design of my other company.

Target Market(s)

Online websites and fortune 500 advertisers- You can see my other company at meadowpixelworks.com

Industry/Entity Type

Advertising

Coding

Coded - Design and coding required

Number of Pages Required

5+ page

Font styles to use
Other font styles liked:
• Be creative

Requirements
Must have
• HTML5, Clean, easy to read, custom graphics, use of video graphics,
• splash 1-2 colors, futuristic, music twist, fun, interesting, looks amazing on a mobile site, extremely professional design. Play into the music theme, vinyl records etc
Nice to have
• Video, interactivity, custom build (not a template)
Should not have
• Flash. I hate stock photos, pages that scroll to much, to many colors (rainbow), sites that don't flow, very templated cookie cutter sites, not mobile compliant.

```html
<!DOCTYPE html>
<html lang="en">
<head>
<meta charset="utf-8">
<title>Quill Trading Desk — Advertising Made Easy</title>
<link href="https://fonts.googleapis.com/css2?family=Montserrat:wght@300;400;600&family=Open+Sans:wght@400;600;700&display=swap" rel="stylesheet">
<style>
:root{
  --accent:#2ba6de;
  --ink:#333b42;
  --muted:#7a8288;
  --band:#ededed;
  --line:#dde2e5;
  --footer:#141414;
  --footer-deep:#0a0a0a;
  --footer-text:#9a9a9a;
  --white:#ffffff;
}
*{box-sizing:border-box;margin:0;padding:0}
html,body{width:1200px;height:2416px;overflow:hidden}
body{font-family:"Open Sans",Arial,sans-serif;color:var(--ink);background:var(--white);position:relative}
h1,h2,h3,.brand,.nav-link{font-family:"Montserrat",Arial,sans-serif}

/* hero */
.hero{position:absolute;left:0;top:0;width:1200px;height:628px;overflow:hidden}
.hero-photo{position:absolute;inset:0;background:linear-gradient(180deg,#6b6a6e 0%,#8a8583 30%,#4a4c52 60%,#2b2d33 100%)}
.hero-shade{position:absolute;inset:0;background:linear-gradient(180deg,rgba(0,0,0,.35),rgba(0,0,0,.1) 40%,rgba(0,0,0,.25))}
.topbar{position:absolute;left:88px;right:88px;top:24px;height:60px;display:flex;align-items:center;justify-content:space-between}
.brand{color:var(--white);line-height:1}
.brand-name{font-size:44px;font-weight:600;letter-spacing:4px;display:block}
.brand-tag{font-size:12px;font-weight:400;letter-spacing:3px;display:block;margin-top:4px;padding-left:6px}
.nav{display:flex;align-items:center;gap:10px}
.nav-link{color:var(--white);font-size:14px;font-weight:600;letter-spacing:1px;padding:6px 14px;text-decoration:none}
.nav-link.is-active{border:2px solid var(--white);border-radius:20px}
.social{display:flex;gap:8px;margin-left:10px}
.social span{width:22px;height:22px;background:var(--white);display:block}
.hero-title{position:absolute;left:0;right:0;top:312px;text-align:center;color:var(--white)}
.hero-title h1{font-size:52px;font-weight:400;letter-spacing:4px}
.hero-title p{font-family:"Montserrat",Arial,sans-serif;font-size:26px;font-weight:600;letter-spacing:2px;margin-top:14px}
.dots{position:absolute;left:0;right:0;top:580px;display:flex;justify-content:center;gap:12px}
.dots span{width:12px;height:12px;border-radius:50%;background:rgba(255,255,255,.55)}
.dots span.on{background:var(--white)}

/* section headings */
.section-title{text-align:center;color:var(--accent);font-size:40px;font-weight:400;letter-spacing:2px}
.section-sub{text-align:center;font-size:17px;font-weight:600;color:var(--ink);margin-top:6px}

/* services */
.services{position:absolute;left:0;top:628px;width:1200px;height:470px}
.services .section-title{margin-top:42px}
.service{position:absolute;width:310px;display:flex;gap:14px}
.service-icon{flex:0 0 54px;height:54px;border-radius:50%;border:2px solid var(--accent);display:flex;align-items:center;justify-content:center}
.service h3{font-size:14px;font-weight:600;letter-spacing:1px;color:var(--ink);margin-top:6px;white-space:nowrap}
.service p{font-size:12px;color:var(--muted);line-height:1.5;margin-top:4px}
.laptop{position:absolute;left:432px;top:170px;width:336px;height:210px;border-radius:10px 10px 4px 4px;background:linear-gradient(180deg,#e8eaec,#c9cdd1)}

/* global scale */
.global{position:absolute;left:0;top:1110px;width:1200px;height:290px;background:var(--band)}
.global-photo{position:absolute;left:88px;top:20px;width:292px;height:250px;background:linear-gradient(135deg,#5a4a3c,#9b8672 55%,#d7d2cc)}
.global-copy{position:absolute;left:420px;top:30px;width:690px}
.global-copy h2{color:var(--accent);font-size:28px;font-weight:400;letter-spacing:1px}
.global-copy p{font-size:13px;color:var(--muted);line-height:1.55;margin-top:12px}
.read-more{color:var(--accent);font-size:13px;display:inline-block;margin-top:12px}

/* blogs */
.blogs{position:absolute;left:0;top:1460px;width:1200px;height:350px}
.blog-row{position:absolute;left:88px;top:80px;display:flex;gap:60px}
.blog{width:306px;text-align:center}
.blog-photo{height:200px}
.blog-photo.a{background:linear-gradient(135deg,#6f93b5,#c6d4de)}
.blog-photo.b{background:linear-gradient(135deg,#d9dde0,#8c97a0)}
.blog-photo.c{background:linear-gradient(135deg,#3b4a5a,#a2acb3)}
.blog h3{font-family:"Open Sans",Arial,sans-serif;font-size:15px;font-weight:400;color:var(--ink);margin-top:14px}
.blog time{display:block;font-size:11px;color:var(--muted);margin-top:6px}

/* partners */
.partners{position:absolute;left:0;top:1826px;width:1200px;height:190px}
.partners .section-title{font-size:34px}
.partner-row{position:absolute;left:88px;right:88px;top:78px;display:flex;justify-content:space-between;align-items:center;height:70px}
.partner{font-family:"Montserrat",Arial,sans-serif;font-size:24px;font-weight:600;color:var(--ink);display:flex;align-items:center;gap:10px}
.partner-mark{width:18px;height:18px;background:var(--ink);display:block}

/* footer */
.footer{position:absolute;left:0;top:2020px;width:1200px;height:340px;background:var(--footer);color:var(--footer-text)}
.footer-brand{position:absolute;left:88px;top:48px;color:var(--white)}
.footer-brand .brand-name{font-size:42px}
.footer-col{position:absolute;top:44px;width:220px}
.footer-col h3{color:var(--white);font-size:14px;font-weight:600;letter-spacing:1px;margin-bottom:14px}
.footer-col li{list-style:none;font-size:12px;line-height:2;padding-left:14px;position:relative}
.footer-col li::before{content:"";position:absolute;left:0;top:10px;width:5px;height:5px;background:var(--accent)}
.footer-col p{font-size:12px;line-height:1.9}
.signup{display:flex;margin-top:12px;width:200px}
.signup span{flex:1;height:30px;border:1px solid #444;font-size:11px;line-height:28px;padding-left:8px;color:#777}
.signup b{width:34px;height:30px;background:var(--accent);display:flex;align-items:center;justify-content:center}
.footer-social{display:flex;gap:10px;margin-top:16px}
.footer-social span{width:30px;height:30px;border-radius:50%;border:1px solid #666;display:block}
.copyright{position:absolute;left:0;top:2360px;width:1200px;height:56px;background:var(--footer-deep);color:var(--footer-text);font-size:12px;text-align:center;line-height:56px}
.copyright .top{position:absolute;right:30px;top:14px;width:28px;height:28px;background:#2a2a2a}
</style>
</head>
<body>

<header class="hero">
  <div class="hero-photo" role="img" aria-label="City skyline of skyscrapers at dusk"></div>
  <div class="hero-shade"></div>
  <div class="topbar">
    <div class="brand"><span class="brand-name">QUILL</span><span class="brand-tag">Trading Desk</span></div>
    <nav class="nav">
      <a class="nav-link is-active">HOME</a>
      <a class="nav-link">ADVERTISERS</a>
      <a class="nav-link">PUBLISHERS</a>
      <a class="nav-link">ABOUT US</a>
      <a class="nav-link">CONTACTS</a>
      <div class="social"><span></span><span></span><span></span></div>
    </nav>
  </div>
  <div class="hero-title">
    <h1>ADVERTISING MADE EASY</h1>
    <p>WITH A UNIFIED BUYING PLATFORM</p>
  </div>
  <div class="dots"><span class="on"></span><span></span><span></span><span></span><span></span></div>
</header>

<section class="services">
  <h2 class="section-title">OUR SERVICES</h2>
  <p class="section-sub">We provide the most powerful service</p>

  <div class="service" style="left:88px;top:190px">
    <div class="service-icon"><svg width="26" height="22" viewBox="0 0 26 22" fill="none" stroke="#2ba6de" stroke-width="2"><rect x="1" y="1" width="24" height="15" rx="1"/><path d="M9 21h8M13 16v5"/></svg></div>
    <div><h3>CROSS-CHANNEL TARGETING</h3><p>We'll help you reach viewers across devices through video, display.</p></div>
  </div>
  <div class="service" style="left:88px;top:310px">
    <div class="service-icon"><svg width="26" height="26" viewBox="0 0 26 26" fill="none" stroke="#2ba6de" stroke-width="2"><circle cx="13" cy="13" r="5"/><path d="M13 2v4M13 20v4M2 13h4M20 13h4M5 5l3 3M18 18l3 3M21 5l-3 3M8 18l-3 3"/></svg></div>
    <div><h3>AUTOMATED BUYING</h3><p>Our unified programmatic marketplace provides efficiency and scale.</p></div>
  </div>

  <div class="laptop" role="img" aria-label="Laptop showing the Quill name on screen"></div>

  <div class="service" style="left:820px;top:190px">
    <div class="service-icon"><svg width="22" height="26" viewBox="0 0 22 26" fill="none" stroke="#2ba6de" stroke-width="2"><rect x="1" y="1" width="20" height="24" rx="1"/><path d="M5 8h12M5 13h12M5 18h8"/></svg></div>
    <div><h3>FULL TRANSPARENCY</h3><p>We think you should know and see the media you're paying for.</p></div>
  </div>
  <div class="service" style="left:820px;top:310px">
    <div class="service-icon"><svg width="26" height="22" viewBox="0 0 26 22" fill="none" stroke="#2ba6de" stroke-width="2"><path d="M2 11l5 5 6-6 6 6 5-5M7 16l3 3M13 10l-4-4-7 5"/></svg></div>
    <div><h3>TRUE PARTNERSHIPS</h3><p>Our goal is to build long lasting relationships to succeed with you.</p></div>
  </div>
</section>

<section class="global">
  <div class="global-photo" role="img" aria-label="Desk with laptop, notebook, coffee and hands at work"></div>
  <div class="global-copy">
    <h2>GLOBAL SCALE WITH ROI TOP OF MIND</h2>
    <p>Today, advertisers want to measure brand engagement. Campaign goals and objectives are defined by it. Quill's team of sophisticated, customized and targeted media planners creates a successful brand initiative. We pride ourselves on being the fastest growing trading desk designed for brands. We will be the highest, and we offer complete transparency.</p>
    <p>Your marketing goals are unique. They deserve more than a repurposed media plan. At Quill we create custom packages that meet your needs with original and analytical programs specific to the goals of your campaign.</p>
    <a class="read-more">Read More »</a>
  </div>
</section>

<section class="blogs">
  <h2 class="section-title">LATEST BLOGS</h2>
  <div class="blog-row">
    <article class="blog"><div class="blog-photo a" role="img" aria-label="Hands typing on a laptop beside a cup"></div><h3>Neque porro quisquam est qui</h3><time>15.08.15 - 10:48pm - 30 offers</time></article>
    <article class="blog"><div class="blog-photo b" role="img" aria-label="Team meeting around a table with papers"></div><h3>Dolorem ipsum quia dolor sit amet</h3><time>15.08.15 - 10:48pm - 30 offers</time></article>
    <article class="blog"><div class="blog-photo c" role="img" aria-label="Business people discussing charts on a screen"></div><h3>Quisquam est qui dolorem</h3><time>15.08.15 - 10:48pm - 30 offers</time></article>
  </div>
</section>

<section class="partners">
  <h2 class="section-title">DELIVERING VALUE TO OUR PARTNERS...</h2>
  <div class="partner-row">
    <span class="partner">Pinecrest</span>
    <span class="partner">Harbor&amp;Loom</span>
    <span class="partner"><i class="partner-mark"></i>Bluefin</span>
    <span class="partner">Corvo</span>
    <span class="partner">Northfield Lending</span>
  </div>
</section>

<footer class="footer">
  <div class="footer-brand brand"><span class="brand-name">QUILL</span><span class="brand-tag">Trading Desk</span></div>
  <div class="footer-col" style="left:420px">
    <h3>LINKS</h3>
    <ul><li>Customer Support</li><li>Documentation</li><li>Resources</li><li>General FAQ</li><li>Disclosures</li></ul>
  </div>
  <div class="footer-col" style="left:640px">
    <h3>GET IN TOUCH</h3>
    <p>Address: 118 Larkspur Lane,<br>Fairhaven</p>
    <p>Phone: 201 555 0144</p>
    <p>Email: info@quillmarketbench.com</p>
  </div>
  <div class="footer-col" style="left:880px">
    <h3>NEWSLETTER</h3>
    <p>Enter your email for fresh updates from us.</p>
    <div class="signup"><span>Enter email</span><b><svg width="12" height="12" viewBox="0 0 12 12" fill="none" stroke="#fff" stroke-width="2"><path d="M2 6h8M6 2l4 4-4 4"/></svg></b></div>
    <div class="footer-social"><span></span><span></span><span></span></div>
  </div>
</footer>
<div class="copyright">Copyright © 2016, All Rights Reserved<span class="top"></span></div>

</body>
</html>
```